FARLOW'S needs a label design for a Moruga Scorpion Pepper Hot Sauce (5oz bottle)

We need a label for a new company based in south Mississippi called FARLOW'S. We have a new hot sauce made from Moruga Scorpion Peppers that's very hot yet has "layers of flavor". The sauce is a deep red color in a clear bottle. We are looking for something simple yet different and will stand out. We would like to limit the design to 3 colors.

It Company

• wide latin?

```html
<!DOCTYPE html>
<html lang="en">
<head>
<meta charset="utf-8">
<title>FARLOW'S Moruga Scorpion Pepper – Label Layouts</title>
<link rel="stylesheet" href="https://fonts.googleapis.com/css2?family=Bodoni+Moda:wght@700&family=PT+Sans+Narrow&family=Open+Sans:wght@800&family=Jost:wght@300&display=swap">
<style>
  :root {
    --ink: #111111;
    --paper: #ffffff;
    --pepper-red: #ee2330;
    --heat-yellow: #fff200;
    --diamond: #231f20;
    --rule: #555555;
    --hatch-tone: #8a8a8a;
    --caption: #333333;
  }
  html, body {
    margin: 0;
    padding: 0;
    width: 1200px;
    height: 1200px;
    overflow: hidden;
    background: var(--paper);
  }
  .board {
    position: relative;
    width: 1200px;
    height: 1200px;
    background: var(--paper);
  }
  .side-bar {
    position: absolute;
    left: 33px;
    top: 0;
    width: 62px;
    height: 1032px;
    background: #000;
  }
  .foot-band {
    position: absolute;
    left: 0;
    top: 1032px;
    width: 1200px;
    height: 168px;
    background: #000;
  }
  .label-art {
    position: absolute;
    left: 0;
    top: 0;
  }
  .brand { font-family: "Bodoni Moda", "Didot", serif; font-weight: 700; fill: var(--ink); }
  .product { font-family: "Bodoni Moda", "Didot", serif; font-weight: 700; fill: var(--ink); }
  .tagline { font-family: "PT Sans Narrow", "Arial Narrow", sans-serif; fill: var(--ink); }
  .heat-word { font-family: "Open Sans", Arial, sans-serif; font-weight: 800; fill: var(--heat-yellow); }
  .frame { fill: none; stroke: var(--ink); stroke-width: 3.5; }
  .divider { stroke: var(--rule); stroke-width: 1; }
  .hatch-band { fill: var(--hatch-tone); }
  .heat-diamond { fill: var(--diamond); }
  .star { fill: var(--pepper-red); }
  .caption {
    position: absolute;
    top: 792px;
    margin: 0;
    font-family: "Jost", "Helvetica Neue", sans-serif;
    font-weight: 300;
    font-size: 24px;
    letter-spacing: 1px;
    color: var(--caption);
  }
  .caption--vertical { left: 163px; }
  .caption--horizontal { left: 579px; }
</style>
</head>
<body>
<main class="board">
  <div class="side-bar"></div>
  <div class="foot-band"></div>

  <svg class="label-art" width="1200" height="1200" viewBox="0 0 1200 1200" xmlns="http://www.w3.org/2000/svg">
    <defs>
      <polygon id="rating-star" class="star" points="0,-11 2.6,-3.6 10.5,-3.4 4.2,1.4 6.5,8.9 0,4.4 -6.5,8.9 -4.2,1.4 -10.5,-3.4 -2.6,-3.6"/>
    </defs>

    <!-- Vertical label -->
    <g class="label label--vertical">
      <rect class="frame" x="165" y="221" width="340" height="549"/>
      <line class="divider" x1="211" y1="221" x2="211" y2="770"/>
      <line class="divider" x1="371" y1="221" x2="371" y2="770"/>
      <line class="divider" x1="416" y1="221" x2="416" y2="660"/>
      <line class="divider" x1="371" y1="660" x2="505" y2="660"/>

      <rect class="hatch-band" x="177" y="233" width="23" height="268" role="img" aria-label="Diagonal hatch stripe band"/>

      <text class="brand" transform="translate(203,740) rotate(-90)" font-size="32" textLength="195" lengthAdjust="spacingAndGlyphs">FARLOW'S</text>
      <text class="product" transform="translate(289,738) rotate(-90)" font-size="48" textLength="488" lengthAdjust="spacingAndGlyphs">MORUGA SCORPION</text>
      <text class="product" transform="translate(341,595) rotate(-90)" font-size="33" letter-spacing="14" textLength="195" lengthAdjust="spacing">PEPPER</text>
      <text class="tagline" transform="translate(408,625) rotate(-90)" font-size="17" textLength="363" lengthAdjust="spacingAndGlyphs">THAT'S VERY HOT YET HAS "LAYERS OF FLAVOR"</text>

      <g class="heat-rating">
        <use href="#rating-star" x="458" y="255"/>
        <use href="#rating-star" x="458" y="283.5"/>
        <use href="#rating-star" x="458" y="311.9"/>
        <use href="#rating-star" x="458" y="340.4"/>
        <use href="#rating-star" x="458" y="368.8"/>
        <use href="#rating-star" x="458" y="397.3"/>
        <use href="#rating-star" x="458" y="425.8"/>
        <use href="#rating-star" x="458" y="454.2"/>
        <use href="#rating-star" x="458" y="482.7"/>
        <use href="#rating-star" x="458" y="511.2"/>
        <use href="#rating-star" x="458" y="539.6"/>
        <use href="#rating-star" x="458" y="568.1"/>
        <use href="#rating-star" x="458" y="596.5"/>
        <use href="#rating-star" x="458" y="625"/>
      </g>

      <polygon class="heat-diamond" points="434,663 485,714 434,765 383,714"/>
      <text class="heat-word" transform="translate(443,714) rotate(-90)" font-size="24" text-anchor="middle">HOT</text>
    </g>

    <!-- Horizontal label -->
    <g class="label label--horizontal">
      <rect class="frame" x="578" y="432" width="549" height="338"/>
      <line class="divider" x1="578" y1="476" x2="1127" y2="476"/>
      <line class="divider" x1="578" y1="636" x2="1127" y2="636"/>
      <line class="divider" x1="689" y1="636" x2="689" y2="770"/>
      <line class="divider" x1="689" y1="681" x2="1127" y2="681"/>

      <text class="brand" x="607" y="468" font-size="33" textLength="195" lengthAdjust="spacingAndGlyphs">FARLOW'S</text>
      <rect class="hatch-band" x="845" y="443" width="270" height="20" role="img" aria-label="Diagonal hatch stripe band"/>

      <text class="product" x="611" y="555" font-size="48" textLength="486" lengthAdjust="spacingAndGlyphs">MORUGA SCORPION</text>
      <text class="product" x="752" y="606" font-size="33" letter-spacing="14" textLength="198" lengthAdjust="spacing">PEPPER</text>

      <polygon class="heat-diamond" points="634,648 685,699 634,750 583,699"/>
      <text class="heat-word" x="634" y="708" font-size="24" text-anchor="middle">HOT</text>

      <text class="tagline" x="724" y="672" font-size="17" textLength="366" lengthAdjust="spacingAndGlyphs">THAT'S VERY HOT YET HAS "LAYERS OF FLAVOR"</text>

      <g class="heat-rating">
        <use href="#rating-star" x="722" y="722"/>
        <use href="#rating-star" x="750.6" y="722"/>
        <use href="#rating-star" x="779.2" y="722"/>
        <use href="#rating-star" x="807.8" y="722"/>
        <use href="#rating-star" x="836.5" y="722"/>
        <use href="#rating-star" x="865.1" y="722"/>
        <use href="#rating-star" x="893.7" y="722"/>
        <use href="#rating-star" x="922.3" y="722"/>
        <use href="#rating-star" x="950.9" y="722"/>
        <use href="#rating-star" x="979.5" y="722"/>
        <use href="#rating-star" x="1008.2" y="722"/>
        <use href="#rating-star" x="1036.8" y="722"/>
        <use href="#rating-star" x="1065.4" y="722"/>
        <use href="#rating-star" x="1094" y="722"/>
      </g>
    </g>
  </svg>

  <p class="caption caption--vertical">Vertical Orientation</p>
  <p class="caption caption--horizontal">Horizontal Orientation</p>
</main>
</body>
</html>
```